Criação de Projeto Combo top of mind para Odonto
" A empresa vai iniciar actividade dentro de algumas semanas e vai funcionar na fase inicial com uma diretora técnica (dentista) e uma técnica auxiliar de saúde. "

```html
<!DOCTYPE html>
<html lang="pt">
<head>
<meta charset="utf-8">
<title>SorriLuz — Cartão de visita e marcação</title>
<link href="https://fonts.googleapis.com/css2?family=Open+Sans:wght@400;600;700&display=swap" rel="stylesheet">
<style>
  :root {
    --page: #eef0f3;
    --card: #ffffff;
    --navy: #24397f;
    --blue: #4a6cc0;
    --ink: #2b3a78;
    --line: #3b5aa8;
  }
  * { box-sizing: border-box; margin: 0; padding: 0; }
  html, body { width: 1200px; height: 1200px; overflow: hidden; }
  body {
    background: var(--page);
    font-family: "Open Sans", Arial, sans-serif;
    color: var(--ink);
    position: relative;
  }
  .card {
    position: absolute;
    background: var(--card);
    border-radius: 26px;
    box-shadow: 0 14px 30px rgba(30, 40, 70, 0.18);
  }

  /* Front */
  .card-front { left: 199px; top: 180px; width: 670px; height: 379px; }
  .brand { position: absolute; left: 0; right: 0; top: 150px; text-align: center; }
  .brand-mark {
    display: inline-block; width: 22px; height: 22px; border-radius: 50%;
    background: var(--navy); vertical-align: middle; margin-right: 10px;
  }
  .brand-name {
    font-weight: 600; font-size: 54px; line-height: 1.1; color: var(--blue);
    vertical-align: middle; letter-spacing: 0.5px;
  }
  .brand-tagline {
    margin-top: 2px; font-size: 15px; letter-spacing: 6px; color: var(--blue);
  }
  .contact { position: absolute; top: 296px; display: flex; align-items: center; gap: 12px; font-size: 15px; line-height: 1.25; color: var(--navy); }
  .contact-phone { left: 108px; }
  .contact-web { left: 324px; }
  .contact svg { width: 22px; height: 22px; flex: none; }
  .contact strong { font-weight: 700; }

  /* Back */
  .card-back { left: 324px; top: 643px; width: 670px; height: 377px; }
  .booking-title { position: absolute; left: 86px; top: 30px; display: flex; align-items: flex-start; gap: 10px; }
  .booking-title svg { width: 36px; height: 36px; }
  .booking-title p { font-size: 18px; line-height: 1.1; color: var(--navy); letter-spacing: 0.5px; }
  .col-head { position: absolute; top: 50px; font-size: 18px; color: var(--navy); }
  .col-date { left: 362px; }
  .col-time { left: 511px; }
  .rows { position: absolute; left: 77px; top: 70px; width: 540px; }
  .row { display: flex; align-items: flex-end; height: 46px; font-size: 16px; color: var(--line); }
  .fill { border-bottom: 2px solid var(--line); display: inline-block; }
  .fill-name { width: 178px; margin-right: 69px; }
  .name-gap { width: 178px; margin-right: 69px; display: inline-block; }
  .fill-day { width: 56px; }
  .fill-month { width: 56px; }
  .sep { padding: 0 2px; }
  .fill-hour { width: 56px; margin-left: 35px; }
  .fill-min { width: 56px; }
  .notice { position: absolute; left: 80px; top: 302px; font-size: 12.5px; line-height: 1.4; color: var(--navy); }
</style>
</head>
<body>
  <section class="card card-front" aria-label="Frente do cartão">
    <div class="brand">
      <span class="brand-mark"></span><span class="brand-name">SorriLuz</span>
      <p class="brand-tagline">MEDICINA DENTÁRIA</p>
    </div>
    <div class="contact contact-phone">
      <svg viewBox="0 0 24 24" aria-hidden="true"><path fill="none" stroke="#24397f" stroke-width="2" stroke-linejoin="round" d="M6 3h3l2 5-2.5 1.5a11 11 0 0 0 6 6L16 13l5 2v3a3 3 0 0 1-3 3A15 15 0 0 1 3 6a3 3 0 0 1 3-3z"/></svg>
      <span>00 90000 0000<br>00 0000 0000</span>
    </div>
    <div class="contact contact-web">
      <svg viewBox="0 0 24 24" aria-hidden="true"><g fill="none" stroke="#24397f" stroke-width="1.8"><circle cx="12" cy="12" r="9"/><ellipse cx="12" cy="12" rx="4" ry="9"/><path d="M3 12h18M5 7h14M5 17h14"/></g></svg>
      <span>ola@sorriluz.pt<br><strong>www.sorriluz.pt</strong></span>
    </div>
  </section>

  <section class="card card-back" aria-label="Verso do cartão">
    <div class="booking-title">
      <svg viewBox="0 0 34 34" aria-hidden="true"><g fill="none" stroke="#24397f" stroke-width="2.4"><rect x="3" y="6" width="24" height="22" rx="2"/><path d="M3 12h24M9 3v6M21 3v6"/><circle cx="25" cy="25" r="6" fill="#fff"/><path d="M25 22v3h2.5"/></g><g fill="#24397f"><rect x="7" y="15" width="3" height="3"/><rect x="12" y="15" width="3" height="3"/><rect x="17" y="15" width="3" height="3"/><rect x="7" y="20" width="3" height="3"/><rect x="12" y="20" width="3" height="3"/></g></svg>
      <p>CONSULTA<br>MARCAÇÃO</p>
    </div>
    <span class="col-head col-date">DATA</span>
    <span class="col-head col-time">HORA</span>
    <div class="rows">
      <div class="row"><span class="fill fill-name"></span><span class="fill fill-day"></span><span class="sep">/</span><span class="fill fill-month"></span><span class="fill fill-hour"></span><span class="sep">:</span><span class="fill fill-min"></span></div>
      <div class="row"><span class="fill fill-name"></span><span class="fill fill-day"></span><span class="sep">/</span><span class="fill fill-month"></span><span class="fill fill-hour"></span><span class="sep">:</span><span class="fill fill-min"></span></div>
      <div class="row"><span class="fill fill-name"></span><span class="fill fill-day"></span><span class="sep">/</span><span class="fill fill-month"></span><span class="fill fill-hour"></span><span class="sep">:</span><span class="fill fill-min"></span></div>
      <div class="row"><span class="fill fill-name"></span><span class="fill fill-day"></span><span class="sep">/</span><span class="fill fill-month"></span><span class="fill fill-hour"></span><span class="sep">:</span><span class="fill fill-min"></span></div>
      <div class="row"><span class="name-gap"></span><span class="fill fill-day"></span><span class="sep">/</span><span class="fill fill-month"></span><span class="fill fill-hour"></span><span class="sep">:</span><span class="fill fill-min"></span></div>
    </div>
    <p class="notice">Caso não possa comparecer,<br>por favor, avise com antecedência</p>
  </section>
</body>
</html>
```